*YO!!! Designers Needed!!* Front Page Cover Needed for a $$Billion Dollar$$ Company

We are a manufacturer of aluminum electrolytic capacitors. We are looking to create a front page cover that will be used on our annual report. We are a publicly listed company and work with many Brellmont 500 companies, so your work will be viewed by the BIG GUNS and EXECUTIVES around the WORLD! If selected, you may be selected for additional work.

The front page cover should be unique. If elegance, modern, bling, and creativity somehow got together and had a child, that's what the cover page would look like!

Inspired Examples attached. Check them out!

www.kovantro.com

Font styles to use
Sans Serif

Requirements
Must have
• 1. Must include the attached logo. Logo size, color, and placement are at your discretion.

2. Should include the text, '2020 Annual Report'

3. The design should incorporate the use of foil and/or be embossed. The foil can be part of the design or can be the full page. See various examples attached for reference.

4. Shall be in A4 size and vertical orientation.
Nice to have
• Feel free to add any icons or stock photos (for example capacitors or circuit boards) if needed.

Be creative here and don't be afraid to be bold! The end product will be printed and budget is not a limiting factor, so feel free to make it extravagant if needed.

Our slogan is "Think Ahead". This slogan can or cannot be part of the theme.

```html
<!DOCTYPE html>
<html lang="en">
<head>
<meta charset="utf-8">
<title>Kovantro 2020 Annual Report Cover</title>
<link rel="stylesheet" href="https://fonts.googleapis.com/css2?family=Montserrat:wght@300;400;600;800&display=swap">
<style>
  :root {
    --ink: #151515;
    --paper: #ffffff;
    --teal-deep: #24c2bc;
    --teal-bright: #2ee6de;
    --teal-band: rgba(255, 255, 255, 0.28);
    --foil-light: #eceeef;
    --foil-mid: #cfd2d4;
    --foil-dark: #a7abae;
    --grey-text: #6d6d6d;
  }
  * { margin: 0; padding: 0; box-sizing: border-box; }
  html, body { width: 900px; height: 1200px; overflow: hidden; }
  body {
    background: var(--paper);
    font-family: "Montserrat", Arial, sans-serif;
    position: relative;
  }
  .cover { position: absolute; inset: 0; background: var(--paper); }
  .top-bar {
    position: absolute; left: 0; top: 0;
    width: 760px; height: 78px;
    background: var(--ink);
  }
  .side-bar {
    position: absolute; left: 0; top: 0;
    width: 44px; height: 560px;
    background: var(--ink);
  }
  .hero-panel {
    position: absolute; left: 44px; top: 40px;
    width: 760px; height: 740px;
    background: linear-gradient(200deg, var(--teal-deep) 0%, var(--teal-bright) 70%, #3aeee4 100%);
  }
  .tagline {
    position: absolute; left: 110px; top: 120px;
    color: var(--paper);
    font-weight: 400; font-size: 26px; line-height: 1.25;
  }
  .tagline .brand-word { font-weight: 600; }
  .headline {
    position: absolute; left: 104px; top: 205px;
    color: var(--paper);
    line-height: 0.9; letter-spacing: 2px;
  }
  .headline .line-think { display: block; font-weight: 300; font-size: 118px; }
  .headline .line-ahead { display: block; font-weight: 800; font-size: 150px; letter-spacing: 4px; }
  .report-band {
    position: absolute; left: 104px; top: 500px;
    padding: 8px 26px;
    background: var(--teal-band);
    color: var(--paper);
    font-size: 52px; white-space: nowrap;
  }
  .report-band .year { font-weight: 800; }
  .report-band .label { font-weight: 400; }
  .foil-photo {
    position: absolute; left: 300px; top: 620px;
    width: 600px; height: 470px;
    background: linear-gradient(160deg, var(--foil-light) 0%, var(--foil-mid) 55%, var(--foil-dark) 100%);
  }
  .brand-lockup {
    position: absolute; left: 410px; top: 800px;
    color: var(--ink);
  }
  .brand-lockup .brand-name {
    display: block;
    font-weight: 800; font-size: 84px; letter-spacing: 1px; line-height: 1;
  }
  .brand-lockup .brand-slogan {
    display: block; text-align: right;
    font-weight: 800; font-size: 20px; letter-spacing: 1px; margin-top: 4px;
  }
  .web-address {
    position: absolute; left: 300px; width: 600px; top: 1128px;
    text-align: center;
    color: var(--grey-text);
    font-weight: 600; font-size: 24px; letter-spacing: 12px;
  }
</style>
</head>
<body>
  <main class="cover">
    <div class="top-bar"></div>
    <div class="side-bar"></div>
    <section class="hero-panel"></section>

    <p class="tagline">We're building capacitors to impact the<br>future of technology.<span class="brand-word">Kovantro</span></p>

    <h1 class="headline">
      <span class="line-think">THINK</span>
      <span class="line-ahead">AHEAD</span>
    </h1>

    <p class="report-band"><span class="year">2020</span> <span class="label">Annual Report</span></p>

    <div class="foil-photo" role="img" aria-label="Photo of two hands unrolling a sheet of aluminium foil from a roll"></div>

    <div class="brand-lockup">
      <span class="brand-name">Kovantro</span>
      <span class="brand-slogan">THINK AHEAD.</span>
    </div>

    <p class="web-address">www.kovantro.com</p>
  </main>
</body>
</html>
```